Corporate Vision/Mission Designs for the Office Walls

What we are looking for:

We are looking for design proposals to frame our mission, vision and values on our office walls

The designs need to be elegant, clean lines, simple, easy to follow and of course, should follow our brand guidelines.

Here's the copy:

For Boardoom:
Vision: Marlow Prestwick ignites people with passion enabling joy and lifetime memories

Mission: We are transforming the way property is bought.

For Garage
Purpose: We connect people with their dreams, turn dreams into reality.

For Entrance
Core Values
Honour
Passion
Sharing
Surprise
Fun

Vision & Mission will go in the boardroom
Core Values : at the Entrance
Purpose: in the Garage meeting room

Attachments to this project include:

a) Photos of the walls where they will go, and the current designs on the walls

b) brand guidelines

Industry/Entity Type

Office

Font styles to use
Decorative

Requirements
Must have
• Follow the brandguidelines, and colors.
• Green / use minimally

```html
<!DOCTYPE html>
<html lang="en">
<head>
<meta charset="utf-8">
<title>Marlow Prestwick — Vision, Mission, Values and Purpose Walls</title>
<link rel="stylesheet" href="https://fonts.googleapis.com/css2?family=Kaushan+Script&family=Tenor+Sans&display=swap">
<style>
  :root {
    --canvas: #ffffff;
    --wall: #e6e4e1;
    --wall-shade: #dcdad6;
    --ink: #575a5f;
    --accent: #5fcfbd;
  }
  * { margin: 0; padding: 0; box-sizing: border-box; }
  html, body { width: 1200px; height: 900px; overflow: hidden; background: var(--canvas); }
  .canvas { position: relative; width: 1200px; height: 900px; }

  .wall {
    position: absolute;
    background: linear-gradient(180deg, var(--wall) 0%, var(--wall-shade) 100%);
    color: var(--ink);
  }
  .wall--boardroom { left: 25px; top: 22px; width: 555px; height: 416px; }
  .wall--entrance  { left: 763px; top: 22px; width: 413px; height: 552px; }
  .wall--garage    { left: 187px; top: 462px; width: 549px; height: 411px; }

  .statement { position: absolute; text-align: center; }
  .heading {
    font-family: "Kaushan Script", cursive;
    font-size: 40px;
    line-height: 1;
    color: var(--ink);
  }
  .heading-swash { display: block; margin: -2px auto 0; }
  .body-copy {
    font-family: "Tenor Sans", sans-serif;
    font-size: 17px;
    letter-spacing: 1.6px;
    line-height: 27.5px;
    margin-top: 24px;
  }

  .statement--vision  { left: 20px; top: 95px; width: 270px; }
  .statement--mission { left: 280px; top: 95px; width: 250px; }

  .statement--values { left: 0; top: 85px; width: 413px; }
  .value-list { list-style: none; margin: 28px auto 0; width: 146px; }
  .value-list li {
    font-family: "Tenor Sans", sans-serif;
    font-size: 27px;
    letter-spacing: 2.5px;
    line-height: 48px;
    border-bottom: 2px solid var(--accent);
    height: 50.5px;
    white-space: nowrap;
    display: flex; justify-content: center;
  }
  .value-list li:last-child { border-bottom: none; }

  .statement--purpose { left: 0; top: 75px; width: 549px; }
  .purpose-lockup { width: 164px; margin: 12px auto 0; font-family: "Tenor Sans", sans-serif; }
  .connector {
    display: flex; align-items: center; gap: 5px;
    font-size: 12px; letter-spacing: 1px; line-height: 18px;
  }
  .connector::before, .connector::after { content: ""; flex: 1; height: 1px; background: var(--ink); }
  .keyword { font-size: 40px; letter-spacing: 1px; line-height: 48px; }
</style>
</head>
<body>
<main class="canvas">

  <section class="wall wall--boardroom" aria-label="Boardroom wall">
    <div class="statement statement--vision">
      <h2 class="heading">Vision</h2>
      <svg class="heading-swash" width="80" height="8" viewBox="0 0 80 8" aria-hidden="true"><path d="M2 6 Q40 0 78 4" stroke="var(--accent)" stroke-width="2.5" fill="none" stroke-linecap="round"/></svg>
      <p class="body-copy">Marlow Prestwick ignites<br>people with passion<br>enabling joy<br>and lifetime memories.</p>
    </div>
    <div class="statement statement--mission">
      <h2 class="heading">Mission</h2>
      <svg class="heading-swash" width="84" height="8" viewBox="0 0 84 8" aria-hidden="true"><path d="M2 6 Q42 0 82 4" stroke="var(--accent)" stroke-width="2.5" fill="none" stroke-linecap="round"/></svg>
      <p class="body-copy">We are transforming<br>the way property<br>is bought.</p>
    </div>
  </section>

  <section class="wall wall--entrance" aria-label="Entrance wall">
    <div class="statement statement--values">
      <h2 class="heading">Core values</h2>
      <svg class="heading-swash" width="140" height="10" viewBox="0 0 140 10" aria-hidden="true"><path d="M2 8 Q70 0 138 4" stroke="var(--accent)" stroke-width="2.5" fill="none" stroke-linecap="round"/></svg>
      <ul class="value-list">
        <li>HONOUR</li>
        <li>PASSION</li>
        <li>SHARING</li>
        <li>SURPRISE</li>
        <li>FUN</li>
      </ul>
    </div>
  </section>

  <section class="wall wall--garage" aria-label="Garage meeting room wall">
    <div class="statement statement--purpose">
      <h2 class="heading" style="font-size:34px">Purpose</h2>
      <svg class="heading-swash" width="80" height="8" viewBox="0 0 80 8" aria-hidden="true"><path d="M2 6 Q40 0 78 4" stroke="var(--accent)" stroke-width="2.5" fill="none" stroke-linecap="round"/></svg>
      <div class="purpose-lockup">
        <p class="connector">We connect</p>
        <p class="keyword">PEOPLE</p>
        <p class="connector">with their</p>
        <p class="keyword">DREAMS</p>
        <p class="connector">turn dreams into</p>
        <p class="keyword">REALITY</p>
      </div>
    </div>
  </section>

</main>
</body>
</html>
```